Quellin Rebranded Website boutique fitness studio

Looking for a simple, easy to navigate, aesthetically pleasing update of our rebranded website

Target Market(s)

Stay at home moms, discretionary income, fitness and wellness

Coding

Coded - Design and coding required

Number of Pages Required

1 page

Font styles to use
Sans Serif

Colors
0054AA
0677BA
7BADD7
CADEEF
E8F1F8

Requirements
Must have
• Snapfeed feed linked, "as seen in" banner, spot for studio video at a later date

```html
<!DOCTYPE html>
<html lang="en">
<head>
<meta charset="utf-8">
<title>Quellin — Elevated Strength</title>
<link href="https://fonts.googleapis.com/css2?family=Quicksand:wght@300;400;500&family=Montserrat:wght@400;500;600;700&display=swap" rel="stylesheet">
<style>
:root{
  --page:#f7fafd;
  --mist:#e8f1f8;
  --sky:#cadeef;
  --soft:#7badd7;
  --mid:#0677ba;
  --deep:#0054aa;
  --navy:#0b2f5e;
  --line:#d6e4f0;
  --ink:#1f2a36;
  --muted:#6a7785;
  --white:#ffffff;
}
*{margin:0;padding:0;box-sizing:border-box}
html,body{width:1200px;height:4107px;overflow:hidden}
body{background:var(--page);font-family:"Montserrat",sans-serif;color:var(--ink);position:relative}
.abs{position:absolute}
.eyebrow{font-size:8.5px;letter-spacing:3px;text-transform:uppercase;color:var(--mid);font-weight:500}
.title{font-family:"Quicksand",sans-serif;font-weight:300;color:var(--ink)}
.link{font-size:8.5px;letter-spacing:2px;text-transform:uppercase;font-weight:600;color:var(--deep);border-bottom:1px solid var(--deep);padding-bottom:2px}
.btn{background:var(--deep);color:var(--white);font-size:9px;letter-spacing:2.4px;font-weight:600;text-transform:uppercase;display:flex;align-items:center;justify-content:center}
.photo{position:absolute}

.nav{position:absolute;left:0;top:0;width:1200px;height:65px;border-bottom:1px solid var(--line);background:var(--page)}
.brand{position:absolute;left:48px;top:21px;display:flex;align-items:center;gap:12px;font-family:"Quicksand",sans-serif;font-weight:500;font-size:14px;letter-spacing:4px;color:var(--navy)}
.brand .dot{width:22px;height:22px;border-radius:50%;background:var(--deep)}
.nav-links{position:absolute;left:273px;top:28px;display:flex;gap:30px;font-size:9px;letter-spacing:2px;font-weight:500;color:var(--ink)}
.login{position:absolute;left:914px;top:28px;font-size:9px;letter-spacing:2px;color:var(--muted)}
.nav-btn{position:absolute;left:974px;top:15px;width:178px;height:36px;border:1px solid var(--deep);font-size:9px;letter-spacing:2px;font-weight:600;color:var(--deep);display:flex;align-items:center;justify-content:center}

.hero-photo{left:0;top:65px;width:1200px;height:517px;background:linear-gradient(100deg,#d8dde2 0%,#c9bcae 30%,#b4683f 45%,#e4e6e8 70%,#eef1f4 100%)}
.hero-card{position:absolute;left:717px;top:124px;width:402px;height:289px;background:var(--page);box-shadow:0 10px 30px rgba(11,47,94,.1);text-align:center}
.hero-card .eyebrow{margin-top:38px}
.hero-card h1{font-family:"Quicksand",sans-serif;font-weight:300;font-size:36px;margin-top:14px;color:var(--ink)}
.hero-card p{font-size:10.5px;line-height:20px;color:#4f5b68;width:330px;margin:12px auto 0}
.hero-card .btn{width:198px;height:34px;margin:18px auto 0}
.hero-card small{display:block;margin-top:14px;font-size:9px;color:var(--muted)}

.method{position:absolute;top:582px;left:0;width:1200px;height:604px;text-align:center;border-bottom:1px solid var(--line)}
.method .eyebrow{position:absolute;top:73px;width:100%}
.method .big{position:absolute;top:93px;width:100%;font-weight:700;font-size:80px;line-height:88px;letter-spacing:12px;color:var(--sky)}
.method .mark{position:absolute;top:366px;width:100%;font-family:"Quicksand",sans-serif;font-size:22px;color:var(--navy);font-weight:500}
.method .lede{position:absolute;top:422px;left:330px;width:540px;font-family:"Quicksand",sans-serif;font-weight:400;font-size:22px;line-height:35px;color:#4f5b68}

.schedule{position:absolute;top:1186px;left:0;width:1200px;height:500px;background:var(--mist)}
.widget{position:absolute;left:81px;top:135px;width:1038px;height:305px;background:var(--white);box-shadow:0 4px 18px rgba(11,47,94,.06)}
.tabs{height:53px;border-bottom:1px solid var(--line);display:flex;align-items:center;padding-left:16px;gap:14px;font-size:8.5px;letter-spacing:1.6px;font-weight:600;color:var(--deep)}
.tabs .on{background:var(--navy);color:var(--white);padding:7px 14px}
.tabs span{padding:7px 8px}
.tabs .tag{margin-left:auto;margin-right:16px;border:1px solid var(--line);color:var(--muted);font-size:7.5px;padding:6px 10px}
.row{height:63px;border-bottom:1px solid var(--line);position:relative;display:flex;align-items:center}
.row:last-child{border-bottom:none}
.row .t{position:absolute;left:20px;font-weight:600;font-size:11px}
.row .c{position:absolute;left:145px;font-family:"Quicksand",sans-serif;font-weight:500;font-size:14px}
.row .w{position:absolute;left:593px;font-size:10px;color:var(--deep)}
.row .s{position:absolute;left:793px;font-size:10px;color:var(--muted)}
.row .b{position:absolute;left:950px;width:68px;height:28px;border:1px solid var(--navy);font-size:8px;letter-spacing:1.6px;font-weight:600;display:flex;align-items:center;justify-content:center}

.cards3{position:absolute;left:81px;top:1851px;display:flex;gap:20px}
.card{width:333px;height:225px;border:1px solid var(--line);text-align:center;background:var(--page)}
.card .n{font-family:"Quicksand",sans-serif;font-size:20px;color:var(--soft);margin-top:32px;font-weight:300}
.card h3{font-family:"Quicksand",sans-serif;font-weight:500;font-size:16px;margin-top:16px}
.card p{font-size:10px;line-height:19px;color:#4f5b68;width:270px;margin:10px auto 0}
.card .link{display:inline-block;margin-top:16px}

.press{position:absolute;top:2393px;left:0;width:1200px;height:127px;background:var(--navy)}
.press .eyebrow{position:absolute;top:39px;width:100%;text-align:center;color:var(--soft)}
.press-list{position:absolute;top:67px;left:11px;display:flex;gap:30px;font-family:"Quicksand",sans-serif;font-size:19px;color:var(--mist);white-space:nowrap;align-items:center}
.press-list i{width:4px;height:4px;border-radius:50%;background:var(--soft);display:inline-block}

.feed{position:absolute;top:2667px;left:81px;display:flex;gap:14px}
.feed div{width:287px;height:191px}

.cta{position:absolute;top:2941px;left:0;width:1200px;height:435px;background:var(--mist)}
.video{position:absolute;left:81px;top:61px;width:655px;height:317px;background:linear-gradient(120deg,#dfe8f0,#b9cfe2 60%,#8fb2d3)}
.video svg{position:absolute;left:297px;top:128px}
.cta-card{position:absolute;left:685px;top:116px;width:434px;height:206px;background:var(--page);box-shadow:0 10px 30px rgba(11,47,94,.1);text-align:center}
.cta-card .eyebrow{margin-top:50px}
.cta-card h2{font-family:"Quicksand",sans-serif;font-weight:300;font-size:28px;margin-top:12px}
.cta-card .btn{width:133px;height:34px;margin:18px auto 0}

.studios{position:absolute;left:81px;top:3528px;display:flex;gap:20px}
.studio{width:333px;height:181px;border:1px solid var(--line);padding:28px 27px}
.studio .eyebrow{color:var(--deep);font-size:7.5px}
.studio h3{font-family:"Quicksand",sans-serif;font-weight:400;font-size:20px;margin-top:6px}
.studio p{font-size:10px;color:#4f5b68;margin-top:12px}
.studio .hrs{font-size:9.5px;color:var(--muted);margin-top:6px}
.studio .link{display:inline-block;margin-top:24px;font-size:7.5px}
.studio.soon .eyebrow{margin-top:18px}
.studio.soon p{font-family:"Quicksand",sans-serif;font-size:14px;line-height:25px;color:var(--ink);margin-top:10px}
.studio.soon .link{margin-top:12px}

.footer{position:absolute;top:3778px;left:0;width:1200px;height:329px;border-top:1px solid var(--line)}
.foot-brand{position:absolute;top:50px;width:100%;text-align:center;font-family:"Quicksand",sans-serif;font-weight:500;font-size:44px;color:var(--navy)}
.foot-tag{position:absolute;top:128px;width:100%;text-align:center;font-size:7px;letter-spacing:1.4px;font-weight:600;color:var(--navy)}
.foot-cols{position:absolute;top:180px;left:0;width:1200px;display:flex}
.foot-cols div{width:300px;text-align:center;font-size:10px;line-height:21px;color:#4f5b68}
.foot-cols .eyebrow{font-size:7.5px;margin-bottom:6px}
.copy{position:absolute;top:4080px;width:100%;text-align:center;font-size:9px;color:var(--muted)}
</style>
</head>
<body>

<header class="nav">
  <div class="brand"><span class="dot"></span>QUELLIN</div>
  <nav class="nav-links"><span>SCHEDULE</span><span>NEW HERE</span><span>PRICING</span><span>THE STUDIO</span><span>INSTRUCTORS</span><span>CONTACT</span></nav>
  <div class="login">LOG IN</div>
  <div class="nav-btn">START — 2 WEEKS $89</div>
</header>

<section>
  <div class="photo hero-photo" role="img" aria-label="Photo of a woman in a rust workout set pulling straps on a reformer machine"></div>
  <div class="hero-card">
    <div class="eyebrow">Welcome to Quellin</div>
    <h1>Elevated Strength.</h1>
    <p>Boutique Tensa in Cedar Hollow &amp; Westbrook, Texas. Forty-five minutes on the Arcformer — low impact, high intensity, no experience needed.</p>
    <div class="btn">Claim the intro offer</div>
    <small>New clients: 2 Weeks Unlimited — $89</small>
  </div>
</section>

<section class="method">
  <div class="eyebrow">Tensa, done beautifully</div>
  <div class="big">THE QUELLIN<br>METHOD</div>
  <div class="mark">Quellin</div>
  <p class="lede">Elevated without feeling exclusive, polished without feeling cold — you'll leave confident, energized, and already looking forward to the next one.</p>
</section>

<section class="schedule">
  <div class="eyebrow abs" style="left:81px;top:62px">This week in the studio</div>
  <h2 class="title abs" style="left:81px;top:80px;font-size:32px">Today's Classes</h2>
  <div class="link abs" style="left:1021px;top:62px">Full schedule</div>
  <div class="widget">
    <div class="tabs"><span class="on">WED 23</span><span>THU 24</span><span>FRI 25</span><span>SAT 26</span><span>SUN 27</span><span>MON 28</span><span>TUE 29</span><span class="tag">SLOTBOOK WIDGET DROPS IN HERE</span></div>
    <div class="row"><span class="t">6:00 AM</span><span class="c">Tensa 45</span><span class="w">w/ Avery</span><span class="s">3 spots left</span><span class="b">BOOK</span></div>
    <div class="row"><span class="t">8:30 AM</span><span class="c">Tensa 45</span><span class="w">w/ Quinn</span><span class="s">7 spots left</span><span class="b">BOOK</span></div>
    <div class="row"><span class="t">12:00 PM</span><span class="c">Tensa 45 · Beginner Friendly</span><span class="w">w/ Rowan</span><span class="s">5 spots left</span><span class="b">BOOK</span></div>
    <div class="row"><span class="t">5:30 PM</span><span class="c">Tensa 45</span><span class="w">w/ Avery</span><span class="s">Waitlist</span><span class="b">BOOK</span></div>
  </div>
</section>

<section>
  <div class="eyebrow abs" style="left:81px;top:1761px">The method</div>
  <h2 class="title abs" style="left:81px;top:1778px;font-size:32px">What is Tensa?</h2>
  <p class="abs" style="left:434px;top:1776px;width:470px;font-size:11px;line-height:21px;color:#4f5b68">Slow, controlled movement under constant tension — strength, cardio and endurance in one class, without the impact. It's hard. You'll love it.</p>
  <div class="cards3">
    <div class="card"><div class="n">01</div><h3>Low impact, high intensity</h3><p>Easy on joints, relentless on muscles. Constant time under tension does the work — no jumping, no pounding.</p><span class="link">Learn more</span></div>
    <div class="card"><div class="n">02</div><h3>On the Arcformer</h3><p>Every class runs on the Arc Pro. Your instructor sets it up and coaches you through — your first class included.</p><span class="link">Learn more</span></div>
    <div class="card"><div class="n">03</div><h3>45 minutes, full body</h3><p>Strength, cardio, core and endurance in one efficient class. Come as you are; leave stronger.</p><span class="link">Learn more</span></div>
  </div>
</section>

<section>
  <div class="photo" style="left:0;top:2142px;width:375px;height:251px;background:linear-gradient(135deg,#e8edf2,#c4ced8)" role="img" aria-label="Photo of clients stretching forward on reformer machines"></div>
  <div class="photo" style="left:375px;top:2142px;width:375px;height:251px;background:linear-gradient(135deg,#dde3e8,#a7b2bd)" role="img" aria-label="Photo of a client in a plank on a reformer machine in a bright studio"></div>
  <div class="photo" style="left:750px;top:2142px;width:375px;height:251px;background:linear-gradient(135deg,#ebe3da,#c8a485)" role="img" aria-label="Photo of a client pulling resistance straps seated on a reformer"></div>
  <div class="photo" style="left:1125px;top:2142px;width:75px;height:251px;background:linear-gradient(135deg,#e4e8ec,#bcc6cf)" role="img" aria-label="Photo of a studio workout"></div>
</section>

<section class="press">
  <div class="eyebrow">The Tensa method, as seen in</div>
  <div class="press-list"><span>Wander Daily</span><i></i><span>Nation Post</span><i></i><span>Ledger</span><i></i><span>Active Living</span><i></i><span>Lumière</span><i></i><span>Form</span><i></i><span>Folk</span><i></i><span>Fit+Kind</span><i></i><span>All</span></div>
</section>

<section>
  <div class="eyebrow abs" style="left:81px;top:2591px">In the studio this week</div>
  <h2 class="title abs" style="left:81px;top:2608px;font-size:32px">@quellintensa</h2>
  <div class="link abs" style="left:1024px;top:2591px">Follow along</div>
  <div class="feed">
    <div role="img" aria-label="Snapfeed post: client in rust set on a reformer" style="background:linear-gradient(135deg,#e8edf2,#c06a40)"></div>
    <div role="img" aria-label="Snapfeed post: clients stretching on reformers" style="background:linear-gradient(135deg,#eef2f6,#c2ccd6)"></div>
    <div role="img" aria-label="Snapfeed post: row of clients on reformers" style="background:linear-gradient(135deg,#e3e8ed,#9faab5)"></div>
    <div role="img" aria-label="Snapfeed post: client side stretching on a reformer" style="background:linear-gradient(135deg,#ebe4dc,#c6a383)"></div>
  </div>
  <p class="abs" style="left:81px;top:2872px;font-size:8.5px;color:var(--muted)">Live feed via FeedFrame, styled to match — auto-updates from Snapfeed.</p>
</section>

<section class="cta">
  <div class="video" role="img" aria-label="Studio video spot: a client side stretching on a reformer in a sunlit studio">
    <svg width="60" height="60" viewBox="0 0 60 60" aria-hidden="true"><circle cx="30" cy="30" r="29" fill="rgba(255,255,255,.85)"/><path d="M25 19 L42 30 L25 41 Z" fill="#0054aa"/></svg>
  </div>
  <div class="cta-card">
    <div class="eyebrow">Your first class is waiting</div>
    <h2>2 Weeks Unlimited — $89</h2>
    <div class="btn">Start today</div>
  </div>
</section>

<section>
  <div class="eyebrow abs" style="left:81px;top:3449px">Find us</div>
  <h2 class="title abs" style="left:81px;top:3466px;font-size:32px">Two Studios, More Coming</h2>
  <div class="studios">
    <div class="studio"><div class="eyebrow">Flagship</div><h3>Cedar Hollow, TX</h3><p>[Street address], Cedar Hollow, TX 77000</p><div class="hrs">Mon–Fri 6a–7p · Sat–Sun 8a–12p</div><span class="link">Directions &amp; parking</span></div>
    <div class="studio"><div class="eyebrow">Now open</div><h3>Westbrook, TX</h3><p>[Street address], Westbrook, TX 77001</p><div class="hrs">Mon–Sat · see schedule</div><span class="link">Directions &amp; parking</span></div>
    <div class="studio soon"><div class="eyebrow">On the horizon</div><p>Millbrook, TX — Fall 2026<br>Stonebridge, TX — Spring 2027</p><span class="link">Get opening updates</span></div>
  </div>
</section>

<footer class="footer">
  <div class="foot-brand">Quellin</div>
  <div class="foot-tag">ELEVATED STRENGTH.</div>
  <div class="foot-cols">
    <div><div class="eyebrow">Contact</div>hello@quellin.example<br>[Phone]</div>
    <div><div class="eyebrow">Hours</div>Mon–Fri 6a–7p<br>Sat–Sun 8a–12p</div>
    <div><div class="eyebrow">Visit us</div>Cedar Hollow, TX · Westbrook, TX<br>Millbrook &amp; Stonebridge soon</div>
    <div><div class="eyebrow">Social</div>Snapfeed · Circlebook</div>
  </div>
</footer>
<div class="copy">© 2026 Quellin · Cedar Hollow &amp; Westbrook, Texas</div>

</body>
</html>
```